Business Card Design for Real Estate Company

I am looking for a business card design that will catch my client's attention.

Industry/Entity Type

Business

Requirements
Must have
• Please have the following information in the business card design. You can substitute the "Office, Mobile, email, and web" with an icon or some other design you may think will go well with the business card.

Derek Osmund
482 W. Fenwick St., Suite 310
Pasadena, CA 91348
Office: 626.748.1196
Mobile: 626.913.4071
email: Derek@CrestviewPropertyWalk.example
web: www.CrestviewPropertyWalk.example

```html
<!DOCTYPE html>
<html lang="en">
<head>
<meta charset="utf-8">
<title>Crestview Property Walk — Business Card</title>
<link rel="stylesheet" href="https://fonts.googleapis.com/css2?family=Josefin+Sans:wght@300;400;600&display=swap">
<style>
  :root {
    --backdrop: #6e6e6e;
    --backdrop-dark: #2c2c2c;
    --card-white: #f7f7f7;
    --brand-brown: #5a4320;
    --blue-deep: #2f6fae;
    --blue-mid: #5aa2dc;
    --blue-light: #8fd3f2;
    --text-light: #ffffff;
    --text-soft: rgba(255,255,255,0.85);
  }
  * { box-sizing: border-box; margin: 0; padding: 0; }
  html, body { width: 1200px; height: 900px; overflow: hidden; }
  body {
    background: radial-gradient(ellipse at 50% 45%, var(--backdrop) 0%, var(--backdrop-dark) 100%);
    font-family: "Josefin Sans", sans-serif;
    position: relative;
  }
  .card {
    position: absolute;
    box-shadow: 0 14px 30px rgba(0,0,0,0.45);
    overflow: hidden;
  }
  /* Front */
  .card-front {
    left: 300px; top: 50px;
    width: 600px; height: 343px;
    background: linear-gradient(180deg, #ffffff 0%, var(--card-white) 100%);
    display: flex; align-items: center; justify-content: center;
  }
  .front-brand {
    display: flex; align-items: center; gap: 16px;
    color: var(--brand-brown);
  }
  .brand-dot {
    width: 22px; height: 22px; border-radius: 50%;
    background: var(--brand-brown);
    flex: none;
  }
  .front-brand .brand-name {
    font-size: 40px; font-weight: 400; letter-spacing: 1px;
  }
  /* Back */
  .card-back {
    left: 250px; top: 440px;
    width: 700px; height: 400px;
    background: linear-gradient(100deg, var(--blue-deep) 0%, var(--blue-mid) 55%, var(--blue-light) 100%);
    color: var(--text-light);
  }
  .name-band {
    position: absolute; left: 0; top: 34px; width: 100%; height: 56px;
    background: linear-gradient(90deg, rgba(255,255,255,0.35) 0%, rgba(255,255,255,0.15) 45%, rgba(255,255,255,0) 70%);
    border-bottom: 3px solid rgba(255,255,255,0.9);
    display: flex; align-items: center; padding-left: 28px; gap: 16px;
  }
  .name-band .brand-dot { width: 18px; height: 18px; background: var(--text-light); }
  .holder-name {
    font-size: 32px; font-weight: 300; letter-spacing: 4px;
  }
  .back-brand {
    position: absolute; right: 36px; top: 108px;
    display: flex; align-items: center; gap: 12px;
  }
  .back-brand .brand-dot { background: var(--text-light); width: 16px; height: 16px; }
  .back-brand .brand-name { font-size: 27px; font-weight: 400; letter-spacing: 1px; }
  .light-stripe {
    position: absolute; left: 0; top: 180px; width: 100%; height: 46px;
    background: linear-gradient(90deg, rgba(255,255,255,0) 30%, rgba(255,255,255,0.6) 60%, #ffffff 85%);
  }
  .address {
    position: absolute; left: 28px; top: 108px;
    display: flex; gap: 10px;
    font-size: 15px; font-weight: 300; line-height: 1.5; letter-spacing: 1px;
    color: var(--text-soft);
  }
  .contact-list {
    position: absolute; left: 260px; top: 250px;
    list-style: none;
    font-size: 16px; font-weight: 300; letter-spacing: 1.5px; line-height: 1.6;
    color: var(--text-soft);
  }
  .contact-list li { display: flex; align-items: center; gap: 10px; }
  .icon { width: 16px; height: 16px; flex: none; fill: none; stroke: currentColor; stroke-width: 1.6; }
</style>
</head>
<body>

<section class="card card-front" aria-label="Card front">
  <div class="front-brand">
    <span class="brand-dot"></span>
    <span class="brand-name">Crestview Property Walk</span>
  </div>
</section>

<section class="card card-back" aria-label="Card back">
  <div class="name-band">
    <span class="brand-dot"></span>
    <span class="holder-name">Derek Osmund</span>
  </div>

  <div class="address">
    <svg class="icon" viewBox="0 0 16 16"><path d="M2 8 L8 2.5 L14 8 M4 7 V14 H12 V7"/></svg>
    <p>482 W. Fenwick St.,<br>Suite 310 Pasadena,<br>CA 91348</p>
  </div>

  <div class="back-brand">
    <span class="brand-dot"></span>
    <span class="brand-name">Crestview Property Walk</span>
  </div>

  <div class="light-stripe"></div>

  <ul class="contact-list">
    <li><svg class="icon" viewBox="0 0 16 16"><path d="M2 6 Q8 1 14 6 L12 8 L10 6.5 H6 L4 8 Z M4 9 H12 V14 H4 Z"/></svg>Office: 626.748.1196</li>
    <li><svg class="icon" viewBox="0 0 16 16"><rect x="4.5" y="1.5" width="7" height="13" rx="1"/><path d="M7 12.5 H9"/></svg>Mobile: 626.913.4071</li>
    <li><svg class="icon" viewBox="0 0 16 16"><rect x="1.5" y="3.5" width="13" height="9"/><path d="M1.5 3.5 L8 9 L14.5 3.5"/></svg>email: Derek@CrestviewPropertyWalk.example</li>
    <li><svg class="icon" viewBox="0 0 16 16"><circle cx="8" cy="8" r="6.5"/><path d="M1.5 8 H14.5 M8 1.5 Q4 8 8 14.5 Q12 8 8 1.5"/></svg>web: www.CrestviewPropertyWalk.example</li>
  </ul>
</section>

</body>
</html>
```